Rise As Captain Book Cover Design

Book Cover Design Brief
Book Title
Rise As Captain
Subtitle
The 10 Quiet Habits of Remarkable Command
Author
Orwen Dalquist
Overview
This book is about leadership that starts within.
Most leadership books focus on tactics or management strategies. This book focuses on the inner disciplines that create powerful leaders — mindset, integrity, focus, empathy, professionalism, honesty, and self-respect.
The tone of the book is bold, direct, confident, and transformational.
This is not a soft or corporate leadership book. It is a call to step up and become the leader you are capable of becoming.
The cover should feel:
• Powerful
• Professional
• Transformational
• Premium
• Memorable
Think best-selling leadership book, not a generic business book.
Target Audience
Business owners
Managers
Entrepreneurs
Team leaders
Professionals who want to grow as leaders
Most readers are ambitious professionals who want to level up their leadership and life.
Design Direction
The design should communicate:
Strength. Discipline. Leadership. Personal transformation.
Avoid cliché leadership visuals like:
• Handshakes
• Office buildings
• Corporate stock imagery
• Teams sitting around tables
The design should feel iconic, bold, and timeless.
Think about covers of successful leadership books such as:
Copper Rituals
Total Stewardship
Won't Break Now
Begin From Purpose
The 36 Rules of Sway
These covers are simple, powerful, and recognizable even at small sizes.
Typography
The title RISE AS CAPTAIN should be:
• Bold
• Strong
• Dominant on the cover
• Easy to read even at small sizes (important for Vellora thumbnails)
The subtitle should be clean and secondary to the title.
The overall typography should feel strong, modern, and premium.
Color Direction
Designers are free to explore colors, but the cover should feel strong and premium, not playful.
Colors that often work well for leadership books include:
Black
Gold
White
Deep blue
Dark red
High contrast and clarity are important.
Style
Preferred style:
• Clean
• Modern
• Minimal
• Strong contrast
Avoid clutter and overly busy designs.
The goal is to create a cover that feels powerful and professional at first glance.
Deliverables
Front cover design for a leadership book.
Final files should include:
• High resolution artwork
• Editable source files
• Print-ready version suitable for publishing
Goal of the Cover
When someone sees this book on Vellora or in a bookstore, they should immediately think:
“This looks like a serious leadership book.”
The design should feel like it belongs next to books by authors such as:
Marcus Thorley
Brandt Osgood
Peter Hollis
Nolan Fairbrook
A strong, confident cover that attracts leaders who want to grow and perform at a higher level.
Target Market(s)
Business Owners and High level managers
Look and feel
Each slider illustrates characteristics of the customer's brand and the style your logo design should communicate.

```html
<!DOCTYPE html>
<html lang="en">
<head>
<meta charset="utf-8">
<title>Rise As Captain — Book Cover</title>
<link rel="stylesheet" href="https://fonts.googleapis.com/css2?family=Barlow+Condensed:wght@700&family=Roboto:wght@400;500&display=swap">
<style>
  :root {
    --page-bg: #161616;
    --cover-bg: #2a2a2a;
    --cover-edge: #232323;
    --title-white: #f2f2f2;
    --text-soft: #e4e4e4;
    --gold: #b8944f;
  }
  html, body {
    margin: 0;
    padding: 0;
    width: 1122px;
    height: 1200px;
    overflow: hidden;
    background: var(--page-bg);
  }
  .cover {
    position: absolute;
    left: 191px;
    top: 30px;
    width: 740px;
    height: 1140px;
    background: linear-gradient(180deg, var(--cover-bg) 0%, var(--cover-edge) 100%);
    box-shadow: 0 10px 40px rgba(0,0,0,0.5);
  }
  .title-svg {
    position: absolute;
    left: 0;
    top: 0;
    width: 740px;
    height: 560px;
  }
  .title-top {
    font-family: "Barlow Condensed", "Arial Narrow", sans-serif;
    font-weight: 700;
    font-size: 76px;
    fill: var(--title-white);
  }
  .title-main {
    font-family: "Barlow Condensed", "Arial Narrow", sans-serif;
    font-weight: 700;
    font-size: 236px;
    fill: var(--title-white);
  }
  .subtitle {
    position: absolute;
    left: 0;
    top: 558px;
    width: 740px;
    margin: 0;
    text-align: center;
    font-family: "Roboto", Arial, sans-serif;
    font-weight: 500;
    font-size: 33px;
    line-height: 48px;
    color: var(--text-soft);
  }
  .author {
    position: absolute;
    left: 0;
    top: 1062px;
    width: 740px;
    margin: 0;
    text-align: center;
    font-family: "Roboto", Arial, sans-serif;
    font-weight: 400;
    font-size: 29px;
    color: var(--text-soft);
  }
</style>
</head>
<body>
  <main class="cover">
    <svg class="title-svg" viewBox="0 0 740 560" aria-labelledby="book-title">
      <title id="book-title">Rise As Captain</title>
      <defs>
        <linearGradient id="gold-rule" x1="0" x2="1" y1="0" y2="0">
          <stop offset="0" stop-color="var(--gold)" stop-opacity="0"/>
          <stop offset="0.5" stop-color="#c9a45e"/>
          <stop offset="1" stop-color="var(--gold)" stop-opacity="0"/>
        </linearGradient>
      </defs>
      <text class="title-top" x="370" y="267" text-anchor="middle">RISE AS</text>
      <rect class="rule" x="96" y="296" width="548" height="2" fill="url(#gold-rule)"/>
      <text class="title-main" x="370" y="502" text-anchor="middle" textLength="562" lengthAdjust="spacingAndGlyphs">CAPTAIN</text>
      <rect class="rule" x="96" y="535" width="548" height="2" fill="url(#gold-rule)"/>
    </svg>
    <p class="subtitle">The 10 Quiet Habits of<br>Remarkable Command</p>
    <p class="author">Orwen Dalquist</p>
  </main>
</body>
</html>
```